Wordpress Theme Design for Glacé-Ember

Hi, I am looking for an awesome WORDPRESS theme for my snoball and coffee business that is called Glacé-Ember. This has to be a wordpress theme, because I have other plugins that I would like to use with this site. I want the design to be professional and sophisticated, but also appeal to kids, because after all, the main focus of the business is going to be snoballs, which kids love. I don't want it to look too much like a kiddy site, though. I am also going to be selling other items such as frito pies, hotdogs, cotton candy, nachos, pickles, candy, toys, etc, but the main focus will be the hot and cold aspect of the coffee and snoballs (hence the name, "Glacé-Ember"). I want the design to look very creative/original and really be attractive to kids, but also very professional so that even adults like coming to the site.
Somewhere in the design I would like to be able to advertise other local businesses in the future, so I would like space incorporated into the design for that. I would also like to be able to add other pages if I want, so there should be space along the top for links, such as "home", "contact", etc. It would also be nice to have a footer in the design for links or other plugins. If you take a look at the site http://wobblypupclipsz.example/, I like the functionality of the site (for example, the layout, links, footer, sidebar on other pages), but obviously there isn't much custom design with the theme.
I actually already have a logo designed that I would like incorporated into the look and feel of the design, so that should give you a good place to start with your design. I want the graphics in the theme to really be eye-catching. You are more than welcome to tweak my current logo, blend it into the theme, whatever...(if you want half of the page to be frozen, and the other half to be fire-ish, doesn't have to be, just giving ideas...any and all designs I will take into consideration). Basically, whatever you think would look amazing.
The more amazing the design, I would definitely give a bonus for.
If this helps you out, I'm not looking for a "glossy" style of wordpress design. I really like how this site (ArtHiveNet) is made. It uses softer, cleaner colors and designs...it's kind of like a "grunge" style with its text and designs (what I mean is it's not a cookie cutter type of design), but nothing too extreme grunge by any means. I'm looking for the same style as the ArtHiveNet site, only with the flare of my type of business.
Hope this helps
Thank you
Updates
Reason: The designs, although nice, are not really what I am looking for. These all just feel like they are ready made templates, and I'm looking for something a little more original and unique.

```html
<!DOCTYPE html>
<html lang="en">
<head>
<meta charset="utf-8">
<title>Glacé-Ember — Snoballs and Coffee</title>
<link rel="stylesheet" href="https://fonts.googleapis.com/css2?family=Gelasio:wght@400;700&family=Tinos&family=Questrial&family=Arimo&family=Share+Tech+Mono&display=swap">
<style>
  :root {
    --header-bg: #ecebec;
    --header-rule: #bdbdbd;
    --ink: #141414;
    --brand: #3a2420;
    --brand-cool: #2fb3e6;
    --nav-bg: #2e2e2e;
    --nav-text: #f2f2f2;
    --nav-active: #e0434b;
    --hot-title: #1d1d1d;
    --cool-title: #1f8fa2;
    --snack-title: #f08a1c;
    --fun-title: #3a9a1e;
    --frame: #d9d9d9;
    --footer-bg: #dcdcdc;
    --footer-ink: #222;
    --contact-bg: #6c6c6c;
    --contact-edge: #8f8f8f;
    --white: #ffffff;
  }
  * { box-sizing: border-box; margin: 0; padding: 0; }
  html, body { width: 900px; height: 1200px; overflow: hidden; }
  body { position: relative; background: var(--white); font-family: "Tinos", "Times New Roman", serif; color: var(--ink); }

  .site-header { position: absolute; left: 0; top: 0; width: 900px; height: 196px; background: var(--header-bg); border-bottom: 6px solid var(--header-rule); }
  .brand { position: absolute; left: 78px; top: 120px; display: flex; align-items: center; gap: 10px; }
  .brand-mark { width: 22px; height: 22px; background: var(--brand-cool); }
  .brand-name { font-family: "Gelasio", Georgia, serif; font-weight: 700; font-size: 36px; color: var(--brand); }

  .main-nav { position: absolute; left: 661px; top: 138px; width: 229px; height: 42px; background: var(--nav-bg); border-radius: 4px; display: flex; align-items: center; padding-left: 10px; font-family: "Questrial", Arial, sans-serif; font-size: 10px; color: var(--nav-text); }
  .main-nav a { color: inherit; text-decoration: none; padding: 0 6px; border-right: 1px solid #555; line-height: 20px; }
  .main-nav a.is-active { box-shadow: inset 0 -2px 0 var(--nav-active); padding: 0; margin-right: 6px; border-right: none; }
  .main-nav .social { display: flex; gap: 2px; margin-left: 6px; }
  .main-nav .social span { width: 15px; height: 15px; background: #7a8fa8; border-radius: 2px; }
  .main-nav .social span:nth-child(2) { background: #b55a52; }
  .main-nav .social span:nth-child(3) { background: #5aa8c8; }

  .zone { position: absolute; left: 0; width: 900px; }
  .zone-hot { top: 196px; height: 241px; background: linear-gradient(90deg, #cdb8ae 0%, #ddd2cc 40%, #f3efed 70%, #fff 100%); }
  .zone-cool { top: 437px; height: 168px; background: linear-gradient(90deg, #fff 0%, #f9fcfd 40%, #e9fbfd 75%, #e4fbfd 100%); }
  .zone-snack { top: 605px; height: 206px; background: linear-gradient(90deg, #fbf1a4 0%, #fdf7cc 35%, #fbfbe2 60%, #eefaf0 85%, #e6fafb 100%); }
  .zone-fun { top: 811px; height: 167px; background: linear-gradient(90deg, #fde6e8 0%, #fbf6e4 22%, #e4fbf4 45%, #e8f3fd 65%, #f1e7fb 100%); }

  .zone-title { position: absolute; z-index: 2; font-family: "Gelasio", Georgia, serif; font-weight: 400; font-size: 34px; line-height: 1; }
  .zone-copy { position: absolute; z-index: 2; font-size: 13.9px; line-height: 16.2px; color: var(--ink); }

  .photo { position: absolute; z-index: 1; border: 5px solid var(--frame); border-radius: 5px; box-shadow: 0 1px 2px rgba(0,0,0,.15); }

  .site-footer { position: absolute; left: 0; top: 978px; width: 900px; height: 222px; background: var(--footer-bg); }
  .footer-links { position: absolute; top: 28px; list-style: none; font-family: "Share Tech Mono", monospace; font-size: 8px; letter-spacing: 0.6px; color: var(--footer-ink); }
  .footer-links li { height: 26px; }
  .footer-features { position: absolute; left: 354px; top: 10px; display: grid; grid-template-columns: 144px 130px; row-gap: 12px; font-family: "Arimo", Arial, sans-serif; font-size: 9px; line-height: 10.5px; color: var(--footer-ink); }
  .feature { display: flex; gap: 5px; height: 28px; }
  .feature svg { flex: none; }
  .contact-card { position: absolute; left: 388px; top: 129px; width: 192px; height: 73px; background: var(--contact-bg); border: 3px solid var(--contact-edge); border-radius: 5px; text-align: center; padding-top: 10px; font-family: "Arimo", Arial, sans-serif; font-size: 9.5px; line-height: 12px; color: var(--white); font-style: normal; }
  .copyright { position: absolute; left: 0; top: 207px; width: 938px; text-align: center; font-family: "Arimo", Arial, sans-serif; font-size: 7px; color: var(--white); }
</style>
</head>
<body>

<header class="site-header">
  <div class="brand"><span class="brand-mark"></span><span class="brand-name">Glacé-Ember</span></div>
  <nav class="main-nav">
    <a class="is-active" href="#">Home</a>
    <a href="#">About US</a>
    <a href="#">Contact Us</a>
    <div class="social" aria-label="Social links"><span></span><span></span><span></span></div>
  </nav>
</header>

<section class="zone zone-hot">
  <div class="photo" role="img" aria-label="Steaming cup of coffee on a saucer with a spoon" style="left:5px;top:36px;width:298px;height:202px;background:radial-gradient(ellipse at 45% 55%, #f1eeec 0%, #c9c3be 40%, #4a2d20 80%, #2b1810 100%);"></div>
  <h2 class="zone-title" style="left:320px;top:40px;color:var(--hot-title)">Hot Zone</h2>
  <p class="zone-copy" style="left:321px;top:80px;width:352px;">Lorem ipsum dolor sit amet, consectetuer adipiscing elit, sed diam nonummy nibh euismod tincidunt ut laoreet dolore magna aliquam erat volutpat. Ut wisi enim ad minim veniam, quis nostrud exerci tation ullamcorper suscipit lobortis nisl ut aliquip ex ea commodo consequat. Duis autem vel eum iriure dolor in hendrerit in vulputate velit esse molestie consequat, vel illum dolore eu feugiat nulla facilisis at vero eros et accumsan et iusto odio dignissim qui blandit praesent luptatum</p>
</section>

<section class="zone zone-cool">
  <h2 class="zone-title" style="left:440px;top:6px;width:218px;text-align:right;color:var(--cool-title)">Cool Zone</h2>
  <p class="zone-copy" style="left:318px;top:45px;width:345px;">Lorem ipsum dolor sit amet, consectetuer adipiscing elit, sed diam nonummy nibh euismod tincidunt ut laoreet dolore magna aliquam erat volutpat. Ut wisi enim ad minim veniam, quis nostrud exerci tation ullamcorper suscipit lobortis nisl ut aliquip ex ea commodo consequat. Duis autem vel eum iriure dolor in hendrerit in vulputate velit esse molestie consequat,</p>
</section>

<section class="zone zone-snack">
  <h2 class="zone-title" style="left:325px;top:8px;color:var(--snack-title)">Snacky</h2>
  <p class="zone-copy" style="left:325px;top:48px;width:362px;">Lorem ipsum dolor sit amet, consectetuer adipiscing elit, sed diam nonummy nibh euismod tincidunt ut laoreet dolore magna aliquam erat volutpat. Ut wisi enim ad minim veniam, quis nostrud exerci tation ullamcorper suscipit lobortis nisl ut aliquip ex ea commodo consequat. Duis autem vel eum iriure dolor in hendrerit in vulputate velit esse molestie consequat, vel illum</p>
</section>

<section class="zone zone-fun">
  <h2 class="zone-title" style="left:520px;top:13px;width:100px;text-align:right;color:var(--fun-title)">Fun</h2>
  <p class="zone-copy" style="left:327px;top:58px;width:362px;">Lorem ipsum dolor sit amet, consectetuer adipiscing elit, sed diam nonummy nibh euismod tincidunt ut laoreet dolore magna aliquam erat volutpat. Ut wisi enim ad minim veniam, quis nostrud exerci tation ullamcorper suscipit lobortis nisl ut aliquip ex ea commodo consequat. Duis autem vel eum iriure dolor in hendrerit in vulputate velit esse molestie consequat, vel illum</p>
</section>

<div class="photo" role="img" aria-label="Pink cotton candy cones" style="left:662px;top:382px;width:149px;height:152px;background:radial-gradient(circle at 45% 40%, #f3b6d2 0%, #f7d6e6 45%, #fff 80%);"></div>
<div class="photo" role="img" aria-label="Ice cream sundae with a cherry" style="left:790px;top:417px;width:90px;height:86px;background:linear-gradient(180deg, #fff 0%, #efe9e4 45%, #7a3a22 80%, #4a2414 100%);"></div>
<div class="photo" role="img" aria-label="Red and orange snoball in a cup on a wooden table" style="left:691px;top:497px;width:195px;height:131px;background:radial-gradient(ellipse at 45% 55%, #d8302a 0%, #e8a02a 35%, #e6e4dc 55%, #8a8578 80%, #6d6a60 100%);"></div>

<div class="photo" role="img" aria-label="Sandwich roll with fresh vegetables" style="left:150px;top:570px;width:165px;height:121px;background:radial-gradient(ellipse at 50% 50%, #9a5a38 0%, #c9a06c 40%, #fff 75%);"></div>
<div class="photo" role="img" aria-label="Plate of pasta with tomatoes" style="left:2px;top:603px;width:170px;height:134px;background:radial-gradient(ellipse at 50% 50%, #c86a2c 0%, #d8a060 45%, #f4ead8 80%);"></div>
<div class="photo" role="img" aria-label="Bowl of fried snack bites" style="left:132px;top:684px;width:170px;height:117px;background:radial-gradient(ellipse at 45% 60%, #b8742c 0%, #8a4a1c 45%, #4a3020 80%, #8a6a4a 100%);"></div>

<div class="photo" role="img" aria-label="Colourful wooden stacking toy" style="left:631px;top:767px;width:159px;height:104px;background:radial-gradient(ellipse at 50% 50%, #e0a040 0%, #6aa8d8 30%, #fff 70%);"></div>
<div class="photo" role="img" aria-label="Wooden toy ark with animal figures" style="left:712px;top:827px;width:174px;height:147px;background:radial-gradient(ellipse at 55% 50%, #c88a4a 0%, #e8c48a 40%, #fff 80%);"></div>

<footer class="site-footer">
  <ul class="footer-links" style="left:150px;">
    <li>Links here links here</li><li>Links here links here</li><li>Links here links here</li><li>Links here links here</li><li>Links here links here</li>
  </ul>
  <ul class="footer-links" style="left:680px;">
    <li>Links here links here</li><li>Links here links here</li><li>Links here links here</li><li>Links here links here</li><li>Links here links here</li>
  </ul>

  <div class="footer-features">
    <div class="feature">
      <svg width="19" height="19" viewBox="0 0 19 19" aria-hidden="true"><rect width="19" height="19" rx="2" fill="#111"/><path d="M4 7h11L9.5 4z M5 8h2v5H5z M8.5 8h2v5h-2z M12 8h2v5h-2z M4 14h11v1.5H4z" fill="#fff"/></svg>
      <span>What;s new,<br>Our speciality</span>
    </div>
    <div class="feature">
      <svg width="19" height="19" viewBox="0 0 19 19" aria-hidden="true"><rect width="19" height="19" rx="2" fill="#111"/><path d="M4 5h11v7H9l-3 3v-3H4z" fill="#fff"/></svg>
      <span style="padding-left:3px">Reviews.</span>
    </div>
    <div class="feature">
      <svg width="19" height="19" viewBox="0 0 19 19" aria-hidden="true"><rect width="19" height="19" rx="2" fill="#111"/><text x="9.5" y="13.5" text-anchor="middle" font-family="Arimo, sans-serif" font-size="9" fill="#fff">$$</text></svg>
      <span>Price List</span>
    </div>
    <div class="feature">
      <svg width="19" height="19" viewBox="0 0 19 19" aria-hidden="true"><rect width="19" height="19" rx="2" fill="#111"/><rect x="8.5" y="8" width="2" height="7" fill="#fff"/><rect x="8.5" y="4.5" width="2" height="2" fill="#fff"/></svg>
      <span>Ideas, Research and<br>innovations.</span>
    </div>
    <div class="feature">
      <svg width="19" height="19" viewBox="0 0 19 19" aria-hidden="true"><rect width="19" height="19" rx="2" fill="#111"/><path d="M4 13l9-8 2 2-9 8H4z" fill="#fff"/></svg>
      <span>Suggestion box</span>
    </div>
    <div class="feature">
      <svg width="19" height="19" viewBox="0 0 19 19" aria-hidden="true"><rect width="19" height="19" rx="2" fill="#111"/><path d="M8.5 4h2v4.5H15v2h-4.5V15h-2v-4.5H4v-2h4.5z" fill="#fff"/></svg>
      <span>Explore your Taste<br>identify your interests.</span>
    </div>
  </div>

  <address class="contact-card">
    Mara &amp; Milo Quillfen<br>
    Harbour Row q-2210<br>
    Ph: 041 7730 5196<br>
    Email: M&amp;M@glace-ember.example
  </address>

  <p class="copyright">© Glacé-Ember | Site designed and hosted by threadpane</p>
</footer>

</body>
</html>
```